Brindle Hollow Jerky packaging

We are looking for a modern, upmarket packaging for our range of beef jerky. Our existing logo is attached for your reference.
We aim to have our product placed in gastro pubs, craft beer events, bottle shops and hotels. The retail package itself will be 60g net and approximately 17cm x 14cm. There will be 4 flavours (original, chilli, smoked pepper and mongolian).
We would like to see some illustration in the design to showcase the different flavours. Use of colour and/or window is optional.

```html
<!DOCTYPE html>
<html lang="en">
<head>
<meta charset="utf-8">
<title>Brindle Hollow Jerky – Pouch Range</title>
<link rel="stylesheet" href="https://fonts.googleapis.com/css2?family=Playfair+Display:wght@400;700&family=Libre+Bodoni:wght@400;700&display=swap">
<style>
  :root{
    --backdrop:#cfcfcf;
    --pouch-dark:#141414;
    --pouch-dark-sheen:#4a4a4a;
    --pouch-light:#f6f6f6;
    --pouch-light-shade:#dcdcdc;
    --ink-dark:#1b1b1b;
    --ink-light:#f2f2f2;
    --accent-red:#c8262b;
    --meat-deep:#3a1a14;
    --meat-warm:#7a3226;
    --sketch-grey:#9a9a9a;
  }
  *{margin:0;padding:0;box-sizing:border-box}
  html,body{width:1200px;height:1151px;overflow:hidden;background:var(--backdrop)}
  .range{position:relative;width:1200px;height:1151px}
  .pouch{position:absolute;top:244px;width:452px;height:668px}
  .pouch--smoked-pepper{left:104px}
  .pouch--original{left:640px}
  .pouch svg{display:block;width:452px;height:668px}
  .brand-name{font-family:"Playfair Display",serif;font-weight:700;font-size:26px;text-anchor:middle}
  .flavour-name{font-family:"Libre Bodoni",serif;font-size:34px;letter-spacing:0.5px}
  .flavour-name--original{font-size:44px}
  .product-type{font-family:"Libre Bodoni",serif;font-size:40px;text-anchor:middle;fill:var(--accent-red)}
  .net-weight{font-family:"Libre Bodoni",serif;font-weight:700;font-size:20px;text-anchor:middle}
</style>
</head>
<body>
<main class="range">

  <section class="pouch pouch--smoked-pepper">
    <svg viewBox="0 0 452 668" xmlns="http://www.w3.org/2000/svg">
      <defs>
        <linearGradient id="darkBody" x1="0" y1="0" x2="1" y2="0.3">
          <stop offset="0" stop-color="var(--pouch-dark)"/>
          <stop offset="0.45" stop-color="var(--pouch-dark-sheen)"/>
          <stop offset="0.7" stop-color="#2a2a2a"/>
          <stop offset="1" stop-color="var(--pouch-dark)"/>
        </linearGradient>
        <linearGradient id="meatDark" x1="0" y1="0" x2="1" y2="1">
          <stop offset="0" stop-color="#2a120d"/>
          <stop offset="0.5" stop-color="var(--meat-deep)"/>
          <stop offset="1" stop-color="#1e0c09"/>
        </linearGradient>
        <linearGradient id="pepperSketch" x1="0" y1="0" x2="1" y2="1">
          <stop offset="0" stop-color="#5a5a5a"/>
          <stop offset="1" stop-color="#2a2a2a"/>
        </linearGradient>
        <path id="arcSmoked" d="M 20 380 Q 232 210 444 380"/>
      </defs>
      <rect class="pouch-body" x="0" y="0" width="452" height="668" rx="4" fill="url(#darkBody)"/>
      <g class="zip-band" stroke="#555" stroke-width="1.5" opacity="0.7">
        <line x1="0" y1="28" x2="452" y2="28"/>
        <line x1="0" y1="62" x2="452" y2="62"/>
        <line x1="0" y1="78" x2="452" y2="78"/>
      </g>
      <text class="brand-name" x="232" y="205" fill="var(--ink-light)">Brindle Hollow Jerky</text>
      <text class="flavour-name" fill="var(--ink-light)"><textPath href="#arcSmoked" startOffset="50%" text-anchor="middle">SMOKED PEPPER</textPath></text>
      <g class="window-frame" fill="none" stroke="var(--ink-light)">
        <rect x="84" y="356" width="296" height="104" stroke-width="3"/>
        <rect x="92" y="364" width="280" height="88" stroke-width="1.5"/>
      </g>
      <rect class="window" x="96" y="368" width="272" height="80" fill="url(#meatDark)" role="img" aria-label="Window showing smoked pepper jerky pieces"/>
      <rect class="flavour-illustration" x="32" y="492" width="136" height="128" rx="10" fill="url(#pepperSketch)" opacity="0.55" role="img" aria-label="Sketch of peppercorns and ground pepper"/>
      <text class="product-type" x="232" y="558">BEEF</text>
      <text class="product-type" x="232" y="598">JERKY</text>
      <text class="net-weight" x="232" y="644" fill="var(--ink-light)">NET.WT.60g</text>
    </svg>
  </section>

  <section class="pouch pouch--original">
    <svg viewBox="0 0 452 668" xmlns="http://www.w3.org/2000/svg">
      <defs>
        <linearGradient id="lightBody" x1="0" y1="0" x2="1" y2="0.3">
          <stop offset="0" stop-color="var(--pouch-light-shade)"/>
          <stop offset="0.3" stop-color="var(--pouch-light)"/>
          <stop offset="0.8" stop-color="#ffffff"/>
          <stop offset="1" stop-color="var(--pouch-light-shade)"/>
        </linearGradient>
        <linearGradient id="meatWarm" x1="0" y1="0" x2="1" y2="1">
          <stop offset="0" stop-color="#5a2418"/>
          <stop offset="0.5" stop-color="var(--meat-warm)"/>
          <stop offset="1" stop-color="#4a1c14"/>
        </linearGradient>
        <linearGradient id="cowSketch" x1="0" y1="0" x2="1" y2="1">
          <stop offset="0" stop-color="#d6d6d6"/>
          <stop offset="1" stop-color="var(--sketch-grey)"/>
        </linearGradient>
        <path id="arcOriginal" d="M 20 380 Q 232 210 444 380"/>
      </defs>
      <rect class="pouch-body" x="0" y="0" width="452" height="668" rx="4" fill="url(#lightBody)"/>
      <g class="zip-band" stroke="#d0d0d0" stroke-width="1.5">
        <line x1="0" y1="28" x2="452" y2="28"/>
        <line x1="0" y1="62" x2="452" y2="62"/>
        <line x1="0" y1="78" x2="452" y2="78"/>
      </g>
      <text class="brand-name" x="232" y="205" fill="var(--ink-dark)">Brindle Hollow Jerky</text>
      <text class="flavour-name flavour-name--original" fill="var(--ink-dark)"><textPath href="#arcOriginal" startOffset="50%" text-anchor="middle">ORIGINAL</textPath></text>
      <g class="window-frame" fill="none" stroke="var(--ink-dark)">
        <rect x="84" y="356" width="296" height="104" stroke-width="3"/>
        <rect x="92" y="364" width="280" height="88" stroke-width="1.5"/>
      </g>
      <rect class="window" x="96" y="368" width="272" height="80" fill="url(#meatWarm)" role="img" aria-label="Window showing original beef jerky pieces"/>
      <rect class="flavour-illustration" x="32" y="488" width="124" height="180" rx="10" fill="url(#cowSketch)" opacity="0.6" role="img" aria-label="Pencil sketch of a cow"/>
      <text class="product-type" x="232" y="558">BEEF</text>
      <text class="product-type" x="232" y="598">JERKY</text>
      <text class="net-weight" x="232" y="644" fill="var(--ink-dark)">NET.WT.60g</text>
    </svg>
  </section>

</main>
</body>
</html>
```